Tovaberry LLC website and online trading portal

Beverage Manufacturing company needs a website design. Should include 5 main pages. Home, Products, About, FAQ and Contact Us. Should also include a shopping cart, online order and shipping page. Company logo is attached.

Target Market(s)

General Public, health conscious individuals

Font styles to use
Serif
Sans Serif
Script

Colors
abd037
fbee3e
ffc214
ffffff

Requirements
Must have
• e-commerce site with 5 main pages. Home, Products, About, FAQ and Contact Us. Should also include a shopping cart, online order and shipping page. Coloscheme should be derived from attached logo

```html
<!DOCTYPE html>
<html lang="en">
<head>
<meta charset="utf-8">
<title>Tovaberry – All Natural Ginger Refreshments</title>
<link href="https://fonts.googleapis.com/css2?family=Domine:wght@400;700&family=Poppins:wght@400;500&display=swap" rel="stylesheet">
<style>
:root{
  --green-dark:#2d8412;
  --green:#5aa821;
  --green-light:#abd037;
  --gold:#c8921b;
  --gold-light:#e0ad2e;
  --yellow:#ffc214;
  --cream:#f1f9e6;
  --navy:#1f2535;
  --ink:#1b1b1b;
  --muted:#6b6b6b;
  --white:#ffffff;
}
*{margin:0;padding:0;box-sizing:border-box}
html,body{width:1200px;height:4490px;overflow:hidden;background:var(--white)}
body{position:relative;font-family:"Poppins",sans-serif;color:var(--ink)}
.abs{position:absolute}
.serif{font-family:"Domine",serif}
.center{text-align:center}
svg{display:block}

/* header */
.brand{left:72px;top:30px;display:flex;align-items:center;gap:10px;font-family:"Domine",serif;font-size:24px;color:var(--yellow);font-weight:700}
.brand .dot{width:30px;height:30px;border-radius:50%;background:var(--yellow)}
.nav{left:390px;top:48px;display:flex;gap:22px;font-size:15px;color:var(--white)}
.nav .active{color:var(--yellow)}
.cart-link{left:832px;top:48px;font-size:15px;color:var(--white);display:flex;gap:8px;align-items:center}
.btn{display:inline-flex;align-items:center;justify-content:center;border-radius:30px;background:linear-gradient(180deg,var(--gold-light),var(--gold));color:var(--white);font-family:"Domine",serif;text-transform:uppercase}
.head-btn{left:973px;top:37px;width:152px;height:46px;font-size:16px}

.hero-title{left:0;width:1200px;top:140px;font-size:40px;line-height:47px;color:var(--white)}
.hero-sub{left:0;width:1200px;top:250px;font-size:16px;color:var(--yellow);font-family:"Domine",serif}
.photo{border-radius:6px}
.order-arc{left:412px;top:714px;width:366px;height:183px;border-radius:183px 183px 0 0;background:linear-gradient(180deg,#dcb75a,var(--gold));color:var(--white);font-family:"Domine",serif;font-size:28px;text-align:center;padding-top:60px}

/* sections */
.sec-title{left:0;width:1200px;font-size:38px;color:var(--ink)}
.sec-text{left:0;width:1200px;font-size:14px;line-height:24px;color:var(--muted)}
.card-img{width:246px;height:270px;background:#ecedec}
.card-name{width:246px;font-family:"Domine",serif;font-size:17px;text-align:center}
.card-sub{width:246px;font-size:14px;color:var(--muted);text-align:center}
.card-price{width:246px;font-size:16px;text-align:center;color:var(--gold);font-weight:500}
.card-price b{color:var(--green-dark);font-weight:500}

.about{left:0;top:1676px;width:1200px;height:600px;background:var(--navy)}
.about-label{left:608px;top:1748px;font-family:"Domine",serif;font-size:20px;color:var(--white)}
.about-title{left:603px;top:1775px;font-family:"Domine",serif;font-size:36px;color:var(--white)}
.about-text{left:608px;top:1862px;width:400px;font-size:14px;line-height:27px;color:#d5d7dd}

.feature{width:300px;text-align:center}
.feature .ic{width:108px;height:108px;border-radius:50%;background:#fbe49a;margin:0 auto}
.feature h3{font-family:"Domine",serif;font-size:20px;margin-top:26px;font-weight:400}
.feature p{font-size:14px;line-height:24px;color:var(--muted);margin-top:8px}

.quote{left:260px;width:680px;top:2798px;font-size:14px;line-height:27px;color:var(--white)}

.field-label{left:601px;font-size:13px;color:var(--muted)}
.field-line{left:601px;width:345px;height:1px;background:#d6d6d6}

.foot-h{font-family:"Domine",serif;font-size:20px;color:var(--white)}
.foot-list{list-style:none;font-size:14px;color:var(--white);line-height:29.5px}
.foot-list li::before{content:"";display:inline-block;width:6px;height:6px;border-radius:50%;background:var(--white);margin-right:16px;vertical-align:middle}
.social{width:44px;height:44px;border-radius:50%;background:rgba(255,255,255,.25)}
</style>
</head>
<body>

<!-- hero background -->
<svg class="abs" style="left:0;top:0" width="1200" height="900" viewBox="0 0 1200 900">
  <defs>
    <radialGradient id="heroGrad" cx="0.5" cy="0.35" r="0.7">
      <stop offset="0" stop-color="#a9d64a"/>
      <stop offset="0.55" stop-color="#4a9c1c"/>
      <stop offset="1" stop-color="#237a0c"/>
    </radialGradient>
  </defs>
  <path d="M0 0 H1200 V320 C1185 500 1110 570 980 565 C850 560 780 490 610 495 C430 500 310 640 160 605 C70 585 20 525 0 470 Z" fill="url(#heroGrad)"/>
</svg>

<div class="abs brand"><span class="dot"></span>Tovaberry</div>
<nav class="abs nav"><span class="active">Home</span><span>Products</span><span>About</span><span>Faq</span><span>Contact Us</span></nav>
<div class="abs cart-link">
  <svg width="20" height="18" viewBox="0 0 20 18" fill="none" stroke="#fff" stroke-width="1.6"><path d="M1 6h18l-2 11H3z M6 6l4-5 4 5"/></svg>Add To Cart</div>
<a class="abs btn head-btn">Order Now</a>

<h1 class="abs hero-title serif center" style="font-weight:700">Delicious &amp; Nutritious Howerver<br>You Healthy</h1>
<p class="abs hero-sub center">All Natural Ginger Refreshments</p>

<div class="abs photo" role="img" aria-label="Ginger juice bottle" style="left:355px;top:395px;width:98px;height:365px;border-radius:30px 30px 6px 6px;background:linear-gradient(180deg,#f2b01a,#f9d873)"></div>
<div class="abs photo" role="img" aria-label="Ginger juice bottle, large centre" style="left:522px;top:287px;width:140px;height:440px;border-radius:40px 40px 6px 6px;background:linear-gradient(180deg,#f5b414,#f8dc86)"></div>
<div class="abs photo" role="img" aria-label="Ginger juice bottle" style="left:752px;top:395px;width:98px;height:365px;border-radius:30px 30px 6px 6px;background:linear-gradient(180deg,#f2b01a,#f9d873)"></div>
<div class="abs photo" role="img" aria-label="Pineapple and ginger root" style="left:65px;top:570px;width:290px;height:140px;border-radius:70px;background:linear-gradient(90deg,#d9b479,#f2c23a)"></div>
<div class="abs photo" role="img" aria-label="Lemon slices, mint and ginger" style="left:955px;top:190px;width:240px;height:160px;border-radius:80px;background:linear-gradient(90deg,#8cc348,#f6d24a)"></div>
<div class="abs photo" role="img" aria-label="Cloves and mint" style="left:830px;top:540px;width:230px;height:140px;border-radius:70px;background:linear-gradient(90deg,#7cb84a,#5b3a25)"></div>
<div class="abs photo" role="img" aria-label="Lime and green apple" style="left:180px;top:250px;width:250px;height:150px;border-radius:75px;background:linear-gradient(90deg,#4f9a24,#8bc34a)"></div>

<div class="abs order-arc">
  <svg width="48" height="50" viewBox="0 0 48 50" fill="none" stroke="#fff" stroke-width="2.4" style="margin:0 auto 14px"><path d="M4 20h40l-5 26H9z M14 20l10-16 10 16 M16 28v12 M24 28v12 M32 28v12"/></svg>
  ORDER NOW
</div>

<!-- products -->
<h2 class="abs sec-title serif center" style="top:955px">Our Products</h2>
<p class="abs sec-text center" style="top:1023px">Lorem Ipsum is simply dummy text of the printing and typesetting industry.<br>Lorem Ipsum has been the industry's standard.</p>

<div class="abs card-img" role="img" aria-label="Bottle with ginger and mint" style="left:77px;top:1106px;background:linear-gradient(180deg,#ecedec 30%,#f4c540 60%,#ecedec 90%)"></div>
<div class="abs card-img" role="img" aria-label="Bottle with ginger and pineapple" style="left:343px;top:1106px;background:linear-gradient(180deg,#ecedec 30%,#f4c540 60%,#ecedec 90%)"></div>
<div class="abs card-img" role="img" aria-label="Bottle with apple and cloves" style="left:610px;top:1106px;background:linear-gradient(180deg,#ecedec 30%,#f4c540 60%,#ecedec 90%)"></div>
<div class="abs card-img" role="img" aria-label="Bottle with lemon and cinnamon" style="left:877px;top:1106px;background:linear-gradient(180deg,#ecedec 30%,#f4c540 60%,#ecedec 90%)"></div>

<div class="abs card-name" style="left:77px;top:1406px">Tovaberry Juice</div>
<div class="abs card-name" style="left:343px;top:1406px">Tovaberry Juice</div>
<div class="abs card-name" style="left:610px;top:1406px">Tovaberry Juice</div>
<div class="abs card-name" style="left:877px;top:1406px">Tovaberry Juice</div>
<div class="abs card-sub" style="left:77px;top:1436px">Ginger Refreshments</div>
<div class="abs card-sub" style="left:343px;top:1436px">Ginger Refreshments</div>
<div class="abs card-sub" style="left:610px;top:1436px">Ginger Refreshments</div>
<div class="abs card-sub" style="left:877px;top:1436px">Ginger Refreshments</div>
<div class="abs card-price" style="left:77px;top:1474px"><b>$39.00</b> | Add To Cart</div>
<div class="abs card-price" style="left:343px;top:1474px"><b>$39.00</b> | Add To Cart</div>
<div class="abs card-price" style="left:610px;top:1474px"><b>$39.00</b> | Add To Cart</div>
<div class="abs card-price" style="left:877px;top:1474px"><b>$39.00</b> | Add To Cart</div>

<div class="abs" style="left:77px;top:1582px;width:1046px;height:1px;background:#e2e2e2"></div>
<a class="abs btn" style="left:516px;top:1558px;width:168px;height:49px;font-size:16px">Order Now</a>

<!-- about -->
<div class="abs about"></div>
<div class="abs" role="img" aria-label="Ginger roots in a wooden tray" style="left:0;top:1676px;width:435px;height:600px;background:linear-gradient(135deg,#5b4128,#d9c5a3 45%,#7e9b4b)"></div>
<svg class="abs" style="left:0;top:2110px" width="1200" height="520" viewBox="0 0 1200 520">
  <path d="M0 170 C80 150 180 80 300 40 C420 0 470 110 560 120 C660 130 720 70 820 95 C920 120 960 100 1060 60 C1130 30 1180 60 1200 80 V520 H0 Z" fill="var(--cream)"/>
</svg>
<div class="abs about-label">About</div>
<div class="abs about-title">Tovaberry Juice</div>
<p class="abs about-text">Lorem Ipsum is simply dummy text of the printing and typesetting industry. Lorem Ipsum has been the industry's standard dummy text ever since the 1500s, when an unknown printer took a galley of type and scrambled it to make a type specimen book. It has survived not only five centuries.</p>
<a class="abs btn" style="left:603px;top:2047px;width:168px;height:50px;font-size:16px">Learn More</a>
<div class="abs" role="img" aria-label="Pineapple slice" style="left:1040px;top:2120px;width:160px;height:150px;border-radius:75px;background:linear-gradient(135deg,#f3c43a,#8f9a3a)"></div>

<!-- features -->
<div class="abs feature" style="left:167px;top:2312px">
  <div class="ic"><svg width="108" height="108" viewBox="0 0 108 108" fill="none" stroke="#2d8412" stroke-width="2.4"><rect x="34" y="38" width="32" height="28" rx="2"/><path d="M66 46h10l8 10v10H66z"/><circle cx="44" cy="70" r="5"/><circle cx="76" cy="70" r="5"/></svg></div>
  <h3>Free Shipping</h3><p>Lorem Ipsum is simply dummy<br>text of the printing.</p>
</div>
<div class="abs feature" style="left:450px;top:2312px">
  <div class="ic"><svg width="108" height="108" viewBox="0 0 108 108" fill="none" stroke="#2d8412" stroke-width="2.4"><path d="M30 68 C30 44 52 36 78 36 C78 62 64 72 44 72 Z M34 70 L66 44"/></svg></div>
  <h3>100% Natural</h3><p>Lorem Ipsum is simply dummy<br>text of the printing.</p>
</div>
<div class="abs feature" style="left:737px;top:2312px">
  <div class="ic"><svg width="108" height="108" viewBox="0 0 108 108" fill="none" stroke="#2d8412" stroke-width="2.4"><rect x="32" y="48" width="46" height="30" rx="3"/><path d="M32 58h46 M55 28l12 5v8c0 6-5 10-12 12-7-2-12-6-12-12v-8z M50 40l4 4 7-7"/></svg></div>
  <h3>Payment Security</h3><p>Lorem Ipsum is simply dummy<br>text of the printing.</p>
</div>

<!-- testimonial -->
<svg class="abs" style="left:0;top:2580px" width="1200" height="440" viewBox="0 0 1200 440">
  <defs><linearGradient id="goldGrad" x1="0" y1="0" x2="1" y2="0"><stop offset="0" stop-color="#c18a1a"/><stop offset="1" stop-color="#c99a2c"/></linearGradient></defs>
  <path d="M0 40 C60 10 120 50 190 30 C260 10 300 55 380 30 C460 5 520 45 600 25 C680 5 740 45 820 28 C900 10 960 45 1040 25 C1110 8 1160 40 1200 20 V440 H0 Z" fill="url(#goldGrad)"/>
</svg>
<div class="abs" role="img" aria-label="Green apple and cloves" style="left:0;top:2550px;width:190px;height:90px;border-radius:45px;background:linear-gradient(90deg,#79b43c,#5a3a25)"></div>
<h2 class="abs sec-title serif center" style="top:2670px">What Our Client Say</h2>
<div class="abs serif center" style="left:0;width:1200px;top:2738px;font-size:56px;line-height:56px;color:var(--green-dark)">&ldquo;</div>
<p class="abs quote center">" Lorem Ipsum is simply dummy text of the printing and typesetting industry. Lorem Ipsum has been the industry's standard dummy text ever since the 1500s, when an unknown printer took a galley of type and scrambled it to make a type "</p>
<div class="abs center" style="left:0;width:1200px;top:2902px;font-size:17px;color:var(--white);font-weight:500">— &nbsp;Client Name</div>
<svg class="abs" style="left:178px;top:2815px" width="20" height="42" viewBox="0 0 20 42" fill="none" stroke="#fff" stroke-width="1.6"><path d="M18 1 L2 21 L18 41"/></svg>
<svg class="abs" style="left:1000px;top:2815px" width="20" height="42" viewBox="0 0 20 42" fill="none" stroke="#fff" stroke-width="1.6"><path d="M2 1 L18 21 L2 41"/></svg>

<!-- newsletter -->
<svg class="abs" style="left:480px;top:3140px" width="580" height="720" viewBox="0 0 580 720">
  <path d="M60 170 C130 40 300 0 420 60 C540 120 570 300 560 420 C550 560 440 690 280 700 C150 708 60 660 40 600" fill="none" stroke="#9ed64a" stroke-width="5"/>
</svg>
<div class="abs" role="img" aria-label="Three juice bottles with pineapple and ginger" style="left:157px;top:3170px;width:400px;height:723px;border-radius:60px 60px 120px 120px;background:linear-gradient(180deg,#f2ad16,#f6d98a 60%,#e9b84a)"></div>
<div class="abs" role="img" aria-label="Lemon slices and mint" style="left:930px;top:3255px;width:130px;height:120px;border-radius:60px;background:linear-gradient(135deg,#6eab35,#f4c83e)"></div>
<h2 class="abs serif center" style="left:560px;width:405px;top:3258px;font-size:31px;line-height:34px;font-weight:700">Sign Up For Our<br>Newsletter</h2>
<p class="abs center" style="left:560px;width:405px;top:3368px;font-size:14px;line-height:26px;color:var(--muted)">Woud you like to receive our exclusive<br>update for signup !</p>
<div class="abs field-label" style="top:3483px">Name *</div>
<div class="abs field-line" style="top:3519px"></div>
<div class="abs field-label" style="top:3565px">Email *</div>
<div class="abs field-line" style="top:3602px"></div>
<a class="abs btn" style="left:669px;top:3629px;width:212px;height:64px;font-size:22px;text-transform:none">SUBSCRIBE</a>

<!-- footer -->
<svg class="abs" style="left:0;top:3900px" width="1200" height="590" viewBox="0 0 1200 590">
  <defs><radialGradient id="footGrad" cx="0.5" cy="0.6" r="0.8"><stop offset="0" stop-color="#8dc63f"/><stop offset="1" stop-color="#2d8412"/></radialGradient></defs>
  <path d="M0 140 C160 90 300 40 470 80 C640 120 760 40 920 70 C1040 95 1120 60 1200 40 V590 H0 Z" fill="url(#footGrad)"/>
</svg>
<div class="abs" role="img" aria-label="Halved lemons" style="left:970px;top:3880px;width:230px;height:180px;border-radius:90px;background:linear-gradient(135deg,#f7d23a,#f2c11f)"></div>

<div class="abs foot-h" style="left:78px;top:4128px">Sitemap</div>
<ul class="abs foot-list" style="left:78px;top:4172px"><li>Home</li><li>Products</li><li>About</li><li>FAQ</li><li>Contact Us</li></ul>
<div class="abs foot-h" style="left:345px;top:4128px">Quick Links</div>
<ul class="abs foot-list" style="left:345px;top:4172px"><li>Privacy Policy</li><li>Tearms &amp; Condition</li><li>Help ?</li><li>Payment Option</li></ul>
<div class="abs foot-h" style="left:611px;top:4128px">Contact Us</div>
<div class="abs" style="left:611px;top:4174px;font-size:14px;color:var(--white);line-height:38px">
  <div style="display:flex;align-items:center;gap:14px"><svg width="18" height="18" viewBox="0 0 18 18" fill="#fff"><path d="M4 1l3 4-2 2c1 3 3 5 6 6l2-2 4 3-2 3C8 17 1 10 1 3z"/></svg>123 456 7890</div>
  <div style="display:flex;align-items:center;gap:14px"><svg width="18" height="14" viewBox="0 0 18 14" fill="#fff"><path d="M0 0h18v14H0z"/><path d="M0 0l9 7 9-7" stroke="#4d9b1f" stroke-width="1.5" fill="none"/></svg>info@tovaberry.example</div>
</div>
<div class="abs social" style="left:612px;top:4258px"></div>
<div class="abs social" style="left:663px;top:4258px"></div>
<div class="abs social" style="left:714px;top:4258px"></div>

<div class="abs" style="left:925px;top:4190px;display:flex;align-items:center;gap:10px;font-family:'Domine',serif;font-size:24px;color:var(--yellow);font-weight:700"><span style="width:28px;height:28px;border-radius:50%;background:var(--yellow);display:inline-block"></span>Tovaberry</div>

<div class="abs" style="left:78px;top:4346px;width:1046px;height:1px;background:rgba(255,255,255,.3)"></div>
<div class="abs center" style="left:0;width:1200px;top:4368px;font-size:14px;color:var(--white)">©Tovaberry -2020 All rights reserved.</div>

</body>
</html>
```